Education related business need name card design

We need name card design for long term study agent.
Company name is Harbor Lantern.
We support clients to connect to the world.
Clients are Japanese family who has primary and secondary school students.

Company Logo is reflection of the globe and HL (Harbor Lantern).
Since business is related to education, we would like to show reliability and love to see the world map (atlas) in the name card.

Target Market(s)

late 30's to 50's parents of primary and secondary students who are enthusiastic for education. Secondary school management

Industry/Entity Type

Education

Contact Information for Business Card

Company name, Address, Official position, Name, Phone number, Mobile number, email address,

Font styles to use
Serif
Other font styles liked:
• Century Gothic(logo)

Requirements
Must have
• Since businee is related to education, we would like to show reliability and love to see the world map (atlas) in the name card.

```html
<!DOCTYPE html>
<html lang="en">
<head>
<meta charset="utf-8">
<title>Harbor Lantern Pte.Ltd. – Name Card</title>
<link rel="stylesheet" href="https://fonts.googleapis.com/css2?family=Questrial&display=swap">
<style>
  :root {
    --navy: #223b7c;
    --accent-blue: #2f7fc8;
    --map-faint: rgba(214, 223, 240, 0.75);
    --map-tone: rgba(150, 172, 220, 0.85);
    --ink: #3a3a3a;
    --ink-soft: #8a8a8a;
    --paper: #ffffff;
    --backdrop: #ececec;
  }
  * { box-sizing: border-box; margin: 0; padding: 0; }
  html, body {
    width: 1200px; height: 1000px; overflow: hidden;
    background: var(--backdrop);
    font-family: "Questrial", "Century Gothic", sans-serif;
  }
  .card {
    position: absolute; left: 190px;
    width: 820px; height: 460px;
    background: var(--paper);
    overflow: hidden;
    box-shadow: 0 6px 18px rgba(0,0,0,0.18);
  }
  .card--back { top: 30px; }
  .card--front { top: 510px; }
  .card__band { position: absolute; inset: 0; width: 100%; height: 100%; }

  .world-map { position: absolute; }
  .card--front .world-map {
    left: 60px; top: 20px; width: 640px; height: 380px;
    background: radial-gradient(closest-side, var(--map-faint) 0%, rgba(214,223,240,0.55) 60%, rgba(214,223,240,0) 100%);
  }
  .card--back .world-map {
    left: 330px; top: 20px; width: 470px; height: 360px;
    background: radial-gradient(closest-side, var(--map-tone) 0%, rgba(150,172,220,0.6) 55%, rgba(150,172,220,0) 100%);
  }

  .brand { position: absolute; display: flex; align-items: center; gap: 14px; }
  .brand__dot { width: 54px; height: 54px; border-radius: 50%; background: var(--accent-blue); flex: none; }
  .brand__name { color: var(--navy); font-size: 30px; line-height: 1.0; font-weight: 400; }
  .card--front .brand { left: 280px; top: 62px; }
  .card--back .brand { left: 40px; top: 150px; }

  .person { position: absolute; left: 150px; top: 192px; }
  .person__name { font-size: 30px; color: var(--ink); line-height: 1.1; }
  .person__role { font-size: 18px; color: var(--ink-soft); margin-top: 2px; }
  .divider { position: absolute; left: 370px; top: 192px; width: 2px; height: 62px; background: var(--ink); }
  .contact { position: absolute; left: 398px; top: 222px; font-size: 21px; color: var(--ink); line-height: 1.3; }
</style>
</head>
<body>

  <section class="card card--back" aria-label="Card back">
    <div class="world-map" role="img" aria-label="World map in soft blue"></div>
    <svg class="card__band" viewBox="0 0 820 460" preserveAspectRatio="none" aria-hidden="true">
      <path d="M0,170 C40,300 170,385 340,385 H820 V460 H0 Z" fill="var(--navy)"/>
    </svg>
    <div class="brand">
      <span class="brand__dot"></span>
      <span class="brand__name">Harbor<br>Lantern Pte.Ltd.</span>
    </div>
  </section>

  <section class="card card--front" aria-label="Card front">
    <div class="world-map" role="img" aria-label="Faint world map in the background"></div>
    <svg class="card__band" viewBox="0 0 820 460" preserveAspectRatio="none" aria-hidden="true">
      <path d="M0,330 H430 C545,330 610,385 650,460 H0 Z" fill="var(--accent-blue)"/>
      <path d="M0,342 H420 C530,342 585,395 615,460 H0 Z" fill="var(--navy)"/>
    </svg>
    <div class="brand">
      <span class="brand__dot"></span>
      <span class="brand__name">Harbor<br>Lantern Pte.Ltd.</span>
    </div>
    <div class="person">
      <p class="person__name">Your Name</p>
      <p class="person__role">Position</p>
    </div>
    <span class="divider"></span>
    <div class="contact">
      <p class="contact__phone">000.000.0000</p>
      <p class="contact__email">name@email.com</p>
    </div>
  </section>

</body>
</html>
```